Surface Protection company needs cards

We are a New Zealand company that will apply nanotechnology coatings on surfaces to prevent growth and spread of bacteria, viruses, mold etc with a sprayer. We deal with large corporates, airlines, hospitals and schools so we are after a new modern, simple and clean look that will have great visual impact.
We a company that is focused on prevention and protection.

Company name, Vela Shield

Subtext, Antimicrobial Surface Protection

Logo, VS

Target Market(s)

Hospitals, Transport agencies, Airlines, Corporate entities

Contact Information for Business Card

Company name, VelaShield
Logo, VS

Gareth Tolley
velashieldnz@postbox.example
+64219305562
www.velashield.example.nz

Requirements
Must have
• Simple clean look.
Nice to have
• We apply nano coatings so try and incorporate this into a theme somehow

```html
<!DOCTYPE html>
<html lang="en">
<head>
<meta charset="utf-8">
<title>VelaShield business cards</title>
<link href="https://fonts.googleapis.com/css2?family=Lato:wght@400;700;900&display=swap" rel="stylesheet">
<style>
  :root {
    --blue: #009fe0;
    --lime: #b8d000;
    --olive: #5c8a2e;
    --ink: #1e1e1e;
    --paper: #ffffff;
    --backdrop: #e4e4e4;
    --pattern: #eeeeee;
  }
  * { margin: 0; padding: 0; box-sizing: border-box; }
  html, body { width: 1200px; height: 1198px; overflow: hidden; }
  body {
    background: var(--backdrop);
    font-family: "Lato", sans-serif;
    color: var(--ink);
    position: relative;
  }
  .card {
    position: absolute;
    left: 342px;
    width: 524px;
    height: 314px;
    background: var(--paper);
    overflow: hidden;
  }
  .card--front { top: 224px; }
  .card--back { top: 634px; }

  .nano-pattern {
    position: absolute;
    top: 0;
    right: 0;
    background: linear-gradient(200deg, var(--pattern) 0%, rgba(238,238,238,0.5) 60%, rgba(255,255,255,0) 100%);
  }
  .card--front .nano-pattern { width: 192px; height: 210px; }
  .card--back .nano-pattern { width: 172px; height: 202px; }

  .brand { position: absolute; display: flex; align-items: center; }
  .brand__mark { background: var(--blue); border-radius: 8px; flex: none; }
  .brand__name {
    font-weight: 900;
    color: var(--blue);
    letter-spacing: -0.5px;
    line-height: 1;
  }
  .brand__tagline {
    font-size: 11px;
    letter-spacing: 0.6px;
    color: var(--ink);
    margin-top: 4px;
  }

  .card--front .brand { left: 36px; top: 32px; }
  .card--front .brand__mark { width: 71px; height: 71px; margin-right: 10px; }
  .card--front .brand__name { font-size: 32px; margin-top: 8px; }

  .divider {
    position: absolute;
    left: 38px;
    top: 120px;
    width: 441px;
    height: 3px;
    background: linear-gradient(90deg, var(--olive), var(--lime));
  }

  .contacts { position: absolute; left: 37px; top: 145px; list-style: none; }
  .contacts li {
    display: flex;
    align-items: center;
    height: 23.3px;
    font-size: 13.5px;
  }
  .contacts svg { width: 18px; height: 18px; margin-right: 8px; flex: none; }

  .person { position: absolute; left: 319px; top: 138px; }
  .person__name { font-size: 22px; font-weight: 900; letter-spacing: 0.2px; }
  .person__role { font-size: 15px; letter-spacing: 2.6px; margin-top: 2px; }

  .band { position: absolute; left: 0; bottom: 0; width: 524px; display: block; }

  .card--back .brand {
    left: 0; right: 0; top: 64px;
    flex-direction: column;
  }
  .card--back .brand__mark { width: 76px; height: 76px; margin-bottom: 12px; }
  .card--back .brand__name { font-size: 36px; }
  .card--back .brand__tagline { font-size: 12px; }
</style>
</head>
<body>

  <section class="card card--front">
    <div class="nano-pattern" role="img" aria-label="Faint molecular lattice pattern"></div>

    <div class="brand">
      <div class="brand__mark"></div>
      <div>
        <div class="brand__name">VELASHIELD</div>
        <div class="brand__tagline">Antimicrobial • Surface • Protection</div>
      </div>
    </div>

    <div class="divider"></div>

    <ul class="contacts">
      <li>
        <svg viewBox="0 0 18 18"><circle cx="9" cy="9" r="9" fill="var(--blue)"/><path d="M9 4.2a3 3 0 0 0-3 3c0 2.3 3 5.8 3 5.8s3-3.5 3-5.8a3 3 0 0 0-3-3z" fill="none" stroke="#fff" stroke-width="1.3"/><circle cx="9" cy="7.2" r="1.1" fill="#fff"/></svg>
        New Zealand
      </li>
      <li>
        <svg viewBox="0 0 18 18"><circle cx="9" cy="9" r="9" fill="var(--blue)"/><rect x="6.4" y="4" width="5.2" height="10" rx="1" fill="none" stroke="#fff" stroke-width="1.3"/><circle cx="9" cy="12.3" r="0.6" fill="#fff"/></svg>
        +64219305562
      </li>
      <li>
        <svg viewBox="0 0 18 18"><circle cx="9" cy="9" r="9" fill="var(--blue)"/><rect x="4.6" y="5.8" width="8.8" height="6.4" rx="0.8" fill="none" stroke="#fff" stroke-width="1.3"/><path d="M4.8 6.2 9 9.4l4.2-3.2" fill="none" stroke="#fff" stroke-width="1.2"/></svg>
        velashieldnz@postbox.example
      </li>
      <li>
        <svg viewBox="0 0 18 18"><circle cx="9" cy="9" r="9" fill="var(--blue)"/><circle cx="9" cy="9" r="4.6" fill="none" stroke="#fff" stroke-width="1.2"/><ellipse cx="9" cy="9" rx="2" ry="4.6" fill="none" stroke="#fff" stroke-width="1"/><path d="M4.4 9h9.2" stroke="#fff" stroke-width="1"/></svg>
        www.velashield.example.nz
      </li>
    </ul>

    <div class="person">
      <div class="person__name">GARETH TOLLEY</div>
      <div class="person__role">Solution Manager</div>
    </div>

    <svg class="band" height="57" viewBox="0 0 524 57" preserveAspectRatio="none">
      <rect width="524" height="57" fill="var(--lime)"/>
      <path d="M0 0H348C330 0 322 6 314 16C306 27 302 32 290 32H0Z" fill="var(--blue)"/>
    </svg>
  </section>

  <section class="card card--back">
    <div class="nano-pattern" role="img" aria-label="Faint molecular lattice pattern"></div>

    <div class="brand">
      <div class="brand__mark"></div>
      <div class="brand__name">VELASHIELD</div>
      <div class="brand__tagline">Antimicrobial • Surface • Protection</div>
    </div>

    <svg class="band" height="60" viewBox="0 0 524 60" preserveAspectRatio="none">
      <rect width="524" height="60" fill="var(--blue)"/>
      <path d="M168 0H524V31H224C210 31 204 26 197 16C189 5 182 0 168 0Z" fill="var(--lime)"/>
    </svg>
  </section>

</body>
</html>
```